Medical device box for kits used for self testing purposes. Attractive simplistic design

Looking for a design that will go on a box that offer multiple range of medical testing ranging from hormones panel to diabetes and thyroid hormones. looking for something attractive and simple to go on a box 6 x 4.5 x 1 inches. attached are some examples from competitors. and our logo that be incorporated with the design.
Picture of the boxes have been attached, pick the color you think goes best with your design.

Target Market(s)

Patients and regular consumers

Industry/Entity Type

Medical

Requirements
Nice to have
• Simple design that is eye catching

```html
<!DOCTYPE html>
<html lang="en">
<head>
<meta charset="utf-8">
<title>Kelvora – Food Sensitivity Comprehensive Test</title>
<link rel="stylesheet" href="https://fonts.googleapis.com/css2?family=Outfit:wght@400;500;600;700&display=swap">
<style>
  :root {
    --backdrop: #e6e8ec;
    --panel: #ffffff;
    --navy: #141c44;
    --accent-yellow: #f2d31b;
    --lavender: #b9b2d8;
    --rose: #f1b3bd;
  }
  html, body {
    margin: 0;
    padding: 0;
    width: 900px;
    height: 1200px;
    overflow: hidden;
    background: var(--backdrop);
    font-family: "Outfit", sans-serif;
    color: var(--navy);
  }
  .box-front {
    position: absolute;
    left: 60px;
    top: 308px;
    width: 780px;
    height: 584px;
    background: var(--panel);
    box-shadow: 0 12px 30px rgba(20, 28, 68, 0.18);
    overflow: hidden;
  }
  .brand {
    position: absolute;
    left: 65px;
    top: 84px;
    display: flex;
    align-items: center;
    gap: 14px;
  }
  .brand-dot {
    width: 30px;
    height: 30px;
    border-radius: 50%;
    background: var(--accent-yellow);
  }
  .brand-name {
    font-size: 58px;
    font-weight: 700;
    line-height: 1;
    color: var(--navy);
    letter-spacing: -0.5px;
  }
  .product-title {
    position: absolute;
    left: 65px;
    top: 236px;
    margin: 0;
    font-size: 37px;
    font-weight: 600;
    line-height: 51px;
    color: var(--navy);
  }
  .title-rule {
    position: absolute;
    left: 65px;
    top: 354px;
    width: 97px;
    height: 3px;
    background: var(--accent-yellow);
  }
  .product-summary {
    position: absolute;
    left: 65px;
    top: 380px;
    margin: 0;
    font-size: 21px;
    font-weight: 400;
    line-height: 27px;
    color: var(--navy);
  }
  .feature-list {
    position: absolute;
    left: 65px;
    top: 497px;
    display: flex;
    gap: 38px;
    margin: 0;
    padding: 0;
    list-style: none;
  }
  .feature {
    display: flex;
    align-items: center;
    gap: 9px;
    font-size: 14px;
    font-weight: 500;
  }
  .feature-badge {
    width: 40px;
    height: 44px;
  }
  .pattern-panel {
    position: absolute;
    left: 519px;
    top: 0;
    width: 261px;
    height: 584px;
    background:
      radial-gradient(ellipse 60% 30% at 45% 48%, rgba(241, 179, 189, 0.55), transparent 75%),
      linear-gradient(180deg, rgba(185, 178, 216, 0.35) 0%, rgba(214, 196, 226, 0.3) 45%, rgba(185, 178, 216, 0.3) 100%);
    -webkit-mask-image: linear-gradient(90deg, transparent 0%, #000 25%, #000 80%, transparent 100%);
            mask-image: linear-gradient(90deg, transparent 0%, #000 25%, #000 80%, transparent 100%);
  }
</style>
</head>
<body>
  <main class="box-front">
    <div class="brand">
      <span class="brand-dot"></span>
      <span class="brand-name">Kelvora</span>
    </div>

    <h1 class="product-title">Food Sensitivity<br>Comprehensive Test</h1>
    <div class="title-rule"></div>
    <p class="product-summary">Lorem ipsum dolor sit amet,<br>consectetur adipiscing elit, sed do</p>

    <ul class="feature-list">
      <li class="feature">
        <svg class="feature-badge" viewBox="0 0 40 44" aria-hidden="true">
          <polygon points="20,2 37,12 37,32 20,42 3,32 3,12" fill="none" stroke="var(--accent-yellow)" stroke-width="2"/>
          <polygon points="20,7 33,14.5 33,29.5 20,37 7,29.5 7,14.5" fill="none" stroke="var(--navy)" stroke-width="1"/>
        </svg>
        <span>Lorem ipsum dolor</span>
      </li>
      <li class="feature">
        <svg class="feature-badge" viewBox="0 0 40 44" aria-hidden="true">
          <polygon points="20,2 37,12 37,32 20,42 3,32 3,12" fill="none" stroke="var(--accent-yellow)" stroke-width="2"/>
          <polygon points="20,7 33,14.5 33,29.5 20,37 7,29.5 7,14.5" fill="none" stroke="var(--navy)" stroke-width="1"/>
        </svg>
        <span>Lorem ipsum dolor</span>
      </li>
    </ul>

    <div class="pattern-panel" role="img" aria-label="Vertical band of linked hexagons holding soft lavender and pink medical icons: heartbeat, heart, cross, DNA strand, doctor, first aid kit and flask"></div>
  </main>
</body>
</html>
```